Wedding and event Photography company.

We need a business card design for a photography company based in Singapore named LumaVek. Our core service offering is wedding photojournalism. We would like to see minimalistic designs that use the colour white. The final design should communicate a sense of ease and reliability.

The attached are a couple of visual reference which i found over the web, i hope it will helps.

Project Brief Update (14th July 2014):
- Please refrain from using any images from the website for the design. The laws and regulations over here does not allow me to distribute my client's images. Thanks!

Target Market(s)

Young and middle aged adults aged 24 - 38. With money to spend =D

Industry/Entity Type

Business

Contact Information for Business Card

Name: Dax Pell
Designation: Head Photographer
Mobile: +65 84126079
Email: tan@lumavek.example
Website: www.lumavek.example

Font styles to use
Other font styles liked:
• Baskerville URW

Colors

Designer to choose colors to be used in the design.

Requirements
Must have
• Must include:
• - The brand LumaVek
• - The logo attached
• - Please help to place the brand LumaVek with the logo according to your preferences.
• - Services
• - Wedding Photography
• - Portraiture
• - Photojournalism
Nice to have
• Looking forward to an elegant and simple design. Please see attached examples!
• Please use Serif Fonts
Should not have
• Please refrain from using dark tones for the majority of the design.
• Please refrain from letterpress and embossing.

```html
<!DOCTYPE html>
<html lang="en">
<head>
<meta charset="utf-8">
<title>LumaVek Business Card</title>
<link rel="stylesheet" href="https://fonts.googleapis.com/css2?family=Josefin+Sans:wght@100;300;600&display=swap">
<style>
  :root {
    --bleed-pink: #ff99ff;
    --guide-line: #1a1a1a;
    --card-white: #ffffff;
    --ink: #000000;
    --label-grey: #4a4a4a;
    --blossom-pink: #e79ad8;
    --blossom-lilac: #c9a6ec;
    --leaf-green: #9ccf7a;
  }
  * { margin: 0; padding: 0; box-sizing: border-box; }
  html, body {
    width: 1200px; height: 708px; overflow: hidden;
    background: var(--card-white);
  }
  .card {
    position: relative; width: 1200px; height: 708px;
    background: var(--card-white);
    font-family: "Josefin Sans", sans-serif;
    overflow: hidden;
  }
  .bleed-band { position: absolute; background: var(--bleed-pink); }
  .bleed-band--top { left: 0; top: 0; width: 1200px; height: 24px; }
  .bleed-band--bottom { left: 0; top: 684px; width: 1200px; height: 24px; }
  .bleed-band--left { left: 0; top: 0; width: 24px; height: 708px; }
  .bleed-band--right { left: 1176px; top: 0; width: 24px; height: 708px; }
  .trim-line { position: absolute; background: var(--guide-line); }
  .trim-line--h { left: 0; width: 1200px; height: 2px; }
  .trim-line--v { top: 0; width: 2px; height: 708px; }
  .safe-frame {
    position: absolute; left: 54px; top: 52px; width: 1094px; height: 603px;
    border: 2px dashed var(--guide-line);
  }
  .guide-label {
    position: absolute; font-size: 13px; color: var(--label-grey);
    font-weight: 300; white-space: nowrap;
  }
  .guide-label strong { font-weight: 600; }
  .guide-label--bleed { right: 30px; top: 4px; }
  .guide-label--safe { right: 58px; top: 58px; }
  .blossom-art {
    position: absolute; left: 808px; top: 415px; width: 368px; height: 269px;
    background:
      radial-gradient(ellipse 30% 22% at 70% 30%, var(--blossom-lilac), transparent 70%),
      radial-gradient(ellipse 35% 25% at 45% 70%, var(--blossom-pink), transparent 70%),
      radial-gradient(ellipse 25% 20% at 85% 70%, var(--blossom-lilac), transparent 70%),
      linear-gradient(150deg, transparent 35%, rgba(156, 207, 122, 0.35) 55%, transparent 75%);
    opacity: 0.9;
  }
  .brand-name {
    position: absolute; left: 0; width: 1200px; top: 235px;
    text-align: center; font-size: 130px; font-weight: 300;
    color: var(--ink); letter-spacing: 2px; line-height: 1;
  }
  .web-address {
    position: absolute; left: 0; width: 1200px; top: 568px;
    text-align: center; font-size: 58px; font-weight: 100;
    color: var(--ink); text-transform: uppercase; line-height: 1;
    letter-spacing: 1px;
  }
</style>
</head>
<body>
  <div class="card">
    <div class="bleed-band bleed-band--top"></div>
    <div class="bleed-band bleed-band--bottom"></div>
    <div class="bleed-band bleed-band--left"></div>
    <div class="bleed-band bleed-band--right"></div>
    <div class="trim-line trim-line--h" style="top:23px"></div>
    <div class="trim-line trim-line--h" style="top:683px"></div>
    <div class="trim-line trim-line--v" style="left:23px"></div>
    <div class="trim-line trim-line--v" style="left:1175px"></div>

    <div class="guide-label guide-label--bleed"><strong>Bleed area:</strong> 3.66″ x 2.16″</div>
    <div class="safe-frame"></div>
    <div class="guide-label guide-label--safe"><strong>Safe area:</strong> 3.34″ x 1.84″</div>

    <div class="blossom-art" role="img" aria-label="Illustration of pink and lilac orchid blossoms on a green stem"></div>

    <div class="brand-name">LumaVek</div>
    <div class="web-address">www.lumavek.example</div>
  </div>
</body>
</html>
```